Business card design for upmarket Home Technology design and Installation company

Hello designers, we need a great business card designed.
We need it to convey high tech, and also sophistication .
We work with some of the most affluent people in the world building them home technology systems, and A/V entertainment systems.

Services offered include the following:
Design, sales, installation, and maintenance of

*Home Automation systems
*Distributed / Multi-Room Audio and Video
*High Performance Networks & WiFi
* Lighting and Shade Control
*Home cinema
*Security and CCTV Systems

I have included a copy of our logo to use for your design efforts.

Target Market(s)

Upmarket clients with multi million euro villas.

Industry/Entity Type

Home technology

Contact Information for Business Card

NAME: Derek Halloran ADDRESS: Plaza Brisa Local 42, Cala Serena, 07392 PHONE: +34-602-518-794 EMAIL: DHalloran@VELTRAsmarthomes.com WEB: www.veltrasmarthomes.com

Requirements
Must have
• Our Logo, and our tagline

```html
<!DOCTYPE html>
<html lang="en">
<head>
<meta charset="utf-8">
<title>VELTRA Refined Living – Business Card</title>
<link rel="stylesheet" href="https://fonts.googleapis.com/css2?family=Montserrat:wght@400;500;700&display=swap">
<style>
  :root {
    --backdrop: #3b3b3b;
    --card: #141414;
    --card-deep: #0c0c0c;
    --gold: #c9a24a;
    --gold-light: #e2c47a;
    --ink: #eaeaea;
    --pattern-a: #2a2a2a;
    --pattern-b: #0d0d0d;
  }
  * { margin: 0; padding: 0; box-sizing: border-box; }
  html, body {
    width: 1200px; height: 801px; overflow: hidden;
    background: var(--backdrop);
    font-family: "Montserrat", sans-serif;
  }
  .canvas {
    position: relative; width: 1200px; height: 801px;
    display: flex; align-items: center; justify-content: center; gap: 40px;
  }
  .card {
    position: relative; width: 540px; height: 309px;
    background: var(--card);
    border: 2px solid var(--gold);
    border-radius: 3px;
    overflow: hidden;
  }

  /* Contact side */
  .card-front { display: flex; align-items: center; padding: 0 30px; }
  .brand { display: flex; flex-direction: column; align-items: flex-start; }
  .card-front .brand { width: 196px; margin-top: 70px; }
  .brand-name {
    font-weight: 500; font-size: 42px; letter-spacing: 5px;
    color: var(--gold); line-height: 1;
  }
  .brand-tagline {
    margin-top: 8px; font-size: 12px; letter-spacing: 3px;
    color: var(--ink); padding-left: 24px; white-space: nowrap;
  }
  .divider { width: 1px; height: 150px; background: var(--gold); margin: 0 20px 0 12px; flex: none; }
  .contact { color: var(--ink); font-size: 12px; line-height: 1.55; white-space: nowrap; }
  .contact-name {
    font-weight: 700; font-size: 15px; letter-spacing: 0.5px;
    color: var(--gold-light); margin-bottom: 4px;
  }
  .contact-address { margin-bottom: 10px; }
  .contact-line { display: flex; align-items: center; gap: 7px; }
  .contact-line svg { width: 10px; height: 10px; flex: none; }

  /* Brand side */
  .card-back { background: var(--card-deep); }
  .pattern-field {
    position: absolute; inset: 0;
    background: linear-gradient(120deg, var(--pattern-a) 0%, #1a1a1a 45%, var(--pattern-b) 100%);
  }
  .back-brand { position: absolute; right: 52px; top: 150px; }
  .back-brand .brand-name { font-size: 50px; letter-spacing: 6px; }
  .back-brand .brand-tagline { font-size: 13px; letter-spacing: 3.4px; padding-left: 22px; }
</style>
</head>
<body>
<main class="canvas">
  <section class="card card-front" aria-label="Business card, contact side">
    <div class="brand">
      <span class="brand-name">VELTRA</span>
      <span class="brand-tagline">Refined Living</span>
    </div>
    <div class="divider"></div>
    <div class="contact">
      <p class="contact-name">DEREK HALLORAN</p>
      <p class="contact-address">Plaza Brisa Local 42<br>Cala Serena, 07392</p>
      <p class="contact-line">
        <svg viewBox="0 0 10 10" aria-hidden="true"><circle cx="5" cy="5" r="5" fill="var(--ink)"/><path d="M3 2.6l1 .1.4 1.2-.6.5a3.6 3.6 0 0 0 1.8 1.8l.5-.6 1.2.4.1 1-.7.5C4.9 7.4 2.6 5.1 2.5 3.3z" fill="var(--card)"/></svg>
        +34-602-518-794
      </p>
      <p class="contact-line">
        <svg viewBox="0 0 10 10" aria-hidden="true"><rect x="0.5" y="2" width="9" height="6" fill="var(--ink)"/><path d="M0.5 2l4.5 3.4L9.5 2" fill="none" stroke="var(--card)" stroke-width="0.8"/></svg>
        DHalloran@VELTRAsmarthomes.com
      </p>
      <p class="contact-line">
        <svg viewBox="0 0 10 10" aria-hidden="true"><circle cx="5" cy="5" r="4.5" fill="var(--ink)"/><path d="M0.5 5h9M5 0.5c-2 2.5-2 6.5 0 9M5 0.5c2 2.5 2 6.5 0 9" fill="none" stroke="var(--card)" stroke-width="0.7"/></svg>
        www.veltrasmarthomes.com
      </p>
    </div>
  </section>

  <section class="card card-back" aria-label="Business card, brand side">
    <div class="pattern-field" role="img" aria-label="Embossed repeating brand symbol pattern in black tones"></div>
    <div class="brand back-brand">
      <span class="brand-name">VELTRA</span>
      <span class="brand-tagline">Refined Living</span>
    </div>
  </section>
</main>
</body>
</html>
```